Wes Hadley Golf Teaching Rack Card

The flyer will be a rack card. Front side only. Nothing on back. 3.75 inches by 8.5 inches. Or close to that. I’d like it to be as colorful as possible and to include several logos in different places.
The brochure is to attract golfers attention and still look traditional and classy not crazy or to artsy. Golf is a very traditional sport and would just like it to look professional and welcoming so golfers no I’m credible in my teaching and they will learn something. I will send a rough idea and a sample of one I had before but use your creative skills and ingenuity to design it. You will have to put my name: Wes Hadley under the NLT logo. It is a requirement by the NLT. Also the logo size must me .0875 inches high. If possible use a gotham or Hoefler text type or something businesslike or similar for my name. Also I am sorry for the different logos available on this file because I am not tech savvy so you will have to choose the best logo and cut it out of the grouping to match what you want to do. I am sorry for all the details. I will be available all weekend if you need more info. or help. I am sure you are very skilled and can tell I am not. Sorry. I laid out a sketch for you so you know what info. verbiage is important. and where to somewhat place the logos. Up to your skill for most of it. Your design! Go for it.!

Target Market(s)

Golfers of all ages from 18-70. Men and Women.

Industry/Entity Type

Golf Industry. Teaching and learning game if golf

Font styles to use
Sans Serif
Other font styles liked:
• Mixture maybe traditional type. Easy to read.

Colors

Designer to choose only greyscale colors for use in the design.

Requirements
Must have
• My JPG golf logo and the NLT official logo. Also will send several other logos to put in. I will tell you where they should go on the rack card.
Nice to have
• Maybe a golf picture from a course with a green and flag as the one on my old brochure I’m sending or similar. It just adds color and eye catching
Should not have
• Nothing hard to read or difficult to comprehend. Pretty straight forward and quality and style in a traditional sense,

```html
<!DOCTYPE html>
<html lang="en">
<head>
<meta charset="utf-8">
<title>Wes Hadley Golf Rack Card</title>
<link rel="stylesheet" href="https://fonts.googleapis.com/css2?family=Montserrat:wght@400;500;600;700;800&display=swap">
<style>
  :root {
    --page: #d9d9d9;
    --white: #ffffff;
    --band-dark: #2e2e2e;
    --accent: #707070;
    --accent-light: #9a9a9a;
    --brand: #3a3a3a;
    --ink: #1f1f1f;
    --grey-text: #444444;
    --partner-light: #7c7c7c;
    --badge-outer: #a8a8a8;
    --badge-inner: #3c3c3c;
    --badge-ring: #2a2a2a;
    --badge-core: #b5b5b5;
  }
  * { margin: 0; padding: 0; box-sizing: border-box; }
  html, body { width: 1200px; height: 2388px; overflow: hidden; }
  body {
    background: var(--page);
    font-family: "Montserrat", sans-serif;
    position: relative;
  }
  .rack-card {
    position: absolute;
    left: 114px; top: 94px;
    width: 972px; height: 2200px;
    background: var(--white);
    overflow: hidden;
    box-shadow: 0 6px 24px rgba(0,0,0,.18);
  }
  .card-shapes { position: absolute; inset: 0; }
  .at { position: absolute; transform: translate(-50%, -50%); white-space: nowrap; text-align: center; }
  .on-dark { color: var(--white); }

  .brand-name {
    position: absolute; right: 58px; top: 70px;
    text-align: right; color: var(--brand);
    font-weight: 600; font-size: 58px; line-height: 1.05; letter-spacing: -1px;
  }

  .section-title { font-weight: 700; font-size: 35px; letter-spacing: 2px; }
  .price-pill {
    background: var(--accent); color: var(--white);
    font-weight: 800; font-size: 30px; border-radius: 26px;
    padding: 4px 34px; letter-spacing: 1px;
  }
  .price-pill sup { font-size: 15px; vertical-align: 12px; }
  .note { font-size: 28px; letter-spacing: 1px; font-weight: 500; }
  .reg { font-weight: 800; font-size: 30px; letter-spacing: 1px; }
  .reg sup { font-size: 15px; vertical-align: 12px; }
  .bullet-dot { color: var(--accent-light); }

  .divider { position: absolute; width: 2px; background: var(--accent-light); }
  .rule { position: absolute; height: 2px; background: var(--accent-light); transform: translateX(-50%); }

  .level-box {
    position: absolute; left: 55px; top: 1006px; width: 406px; height: 226px;
    border: 2px solid var(--accent-light); border-radius: 34px;
    color: var(--white); text-align: center; font-size: 30px; line-height: 1.22;
    padding-top: 26px;
  }
  .level-box .strong { font-weight: 700; }
  .level-box .info { margin-top: 22px; font-weight: 500; }

  .includes-pill {
    background: var(--accent); color: var(--white);
    font-weight: 700; font-size: 24px; letter-spacing: 2px;
    border-radius: 20px; padding: 3px 20px;
  }
  .feature-list {
    position: absolute; left: 515px; top: 1058px;
    list-style: none; color: var(--white); font-size: 26px; line-height: 39px;
    letter-spacing: 1px; font-weight: 500;
  }
  .feature-list li { position: relative; padding-left: 26px; }
  .feature-list li::before {
    content: ""; position: absolute; left: 2px; top: 15px;
    width: 10px; height: 10px; border-radius: 50%; background: var(--accent-light);
  }
  .feature-list .wrap { line-height: 28px; }

  .partner { font-weight: 800; font-size: 74px; letter-spacing: -1px; }
  .partner-motion { color: var(--partner-light); }
  .partner-track { color: var(--ink); }

  .package-list { font-size: 26px; line-height: 31px; letter-spacing: 1px; font-weight: 500; }

  .credential { color: var(--grey-text); font-size: 24px; line-height: 29px; letter-spacing: 1px; }
  .footer-text { color: var(--white); font-size: 26px; letter-spacing: 1px; font-weight: 500; }
  .footer-text.strong { font-weight: 700; }
  .footer-sep { color: rgba(255,255,255,.7); font-size: 24px; }
</style>
</head>
<body>
  <main class="rack-card">
    <svg class="card-shapes" viewBox="0 0 972 2200" width="972" height="2200">
      <defs>
        <linearGradient id="courseTones" x1="0" y1="0" x2="0" y2="1">
          <stop offset="0" stop-color="#ececec"/>
          <stop offset="0.38" stop-color="#c4c4c4"/>
          <stop offset="0.52" stop-color="#8c8c8c"/>
          <stop offset="1" stop-color="#7a7a7a"/>
        </linearGradient>
      </defs>
      <rect class="course-photo" x="0" y="0" width="972" height="920" fill="url(#courseTones)" role="img" aria-label="Photo of a golf green with a flag and a golf bag of clubs beside the hole"/>
      <path class="swing-band-edge" d="M0 663 Q486 888 972 647 L972 1000 L0 1000 Z" fill="var(--accent-light)"/>
      <path class="swing-band" d="M0 679 Q486 905 972 663 L972 1193 Q486 1392 0 1264 Z" fill="var(--band-dark)"/>
      <path class="swing-band-line" d="M0 1280 Q486 1410 972 1208" fill="none" stroke="var(--accent-light)" stroke-width="3"/>
      <path class="lesson-band-edge" d="M0 1552 Q486 1326 972 1520 L972 1817 L0 1817 Z" fill="var(--accent-light)"/>
      <path class="lesson-band" d="M0 1568 Q486 1350 972 1537 L972 1817 L0 1817 Z" fill="var(--band-dark)"/>
      <rect class="lesson-band-line" x="0" y="1817" width="972" height="8" fill="var(--accent-light)"/>
      <rect class="contact-band" x="0" y="2095" width="972" height="105" fill="var(--accent)"/>

      <circle class="badge-guarantee" cx="182" cy="1947" r="81" fill="var(--badge-outer)"/>
      <circle cx="182" cy="1947" r="64" fill="var(--badge-inner)"/>
      <circle class="badge-association" cx="792" cy="1920" r="72" fill="var(--badge-ring)"/>
      <circle cx="792" cy="1920" r="52" fill="var(--badge-core)"/>

      <g class="contact-icons" fill="var(--band-dark)" stroke="var(--white)" stroke-width="2">
        <circle cx="182" cy="2095" r="22"/>
        <circle cx="488" cy="2095" r="22"/>
        <circle cx="792" cy="2095" r="22"/>
      </g>
      <g fill="none" stroke="var(--white)" stroke-width="2.2" stroke-linejoin="round" stroke-linecap="round">
        <rect x="172" y="2088" width="20" height="14" rx="1"/>
        <path d="M172 2089 L182 2097 L192 2089"/>
        <path d="M481 2086 Q479 2096 490 2104 L494 2101 L490 2097 L487 2099 Q484 2096 484 2092 L487 2090 L485 2085 Z"/>
        <circle cx="792" cy="2095" r="10"/>
        <ellipse cx="792" cy="2095" rx="4.5" ry="10"/>
        <path d="M782 2095 H802"/>
      </g>
    </svg>

    <div class="brand-name">WES HADLEY<br>GOLF</div>

    <!-- Swing analysis offer -->
    <div class="at on-dark section-title" style="left:486px; top:828px;">GOLF SWING ANALYSIS</div>
    <div class="at price-pill" style="left:257px; top:888px;"><sup>$</sup>59<sup>99</sup></div>
    <div class="at on-dark note" style="left:257px; top:947px;">(1-Hour Analysis)</div>
    <div class="divider" style="left:487px; top:861px; height:97px;"></div>
    <div class="at on-dark note" style="left:713px; top:885px;"><span class="bullet-dot">•</span>One Time Limited Offer</div>
    <div class="rule" style="left:713px; top:913px; width:60px;"></div>
    <div class="at on-dark reg" style="left:713px; top:944px;">REG <sup>$</sup>79<sup>00</sup></div>

    <div class="level-box">
      <div class="strong">Beginners</div>
      <div>to <span class="strong">Advanced</span></div>
      <div class="info">Additional Info @<br>WWW.<span class="strong">WHADLEY</span>.COM</div>
    </div>

    <div class="at includes-pill" style="left:604px; top:1024px;">INCLUDES</div>
    <ul class="feature-list">
      <li>Swing Analysis w/Video</li>
      <li>Review Of Swing Technique</li>
      <li>Suggested Tips &amp; Drills</li>
      <li class="wrap">Video and Summary sent to<br>your mobile devices</li>
    </ul>

    <!-- Partners -->
    <div class="at partner partner-motion" style="left:304px; top:1384px;">Motionly</div>
    <div class="at partner partner-track" style="left:680px; top:1384px;">Trackora</div>

    <!-- Lesson package -->
    <div class="at on-dark section-title" style="left:486px; top:1526px;">SPECIAL LESSON PACKAGE</div>
    <div class="at on-dark note" style="left:257px; top:1582px; font-size:26px;">3-ONE HOUR LESSONS</div>
    <div class="rule" style="left:257px; top:1610px; width:60px;"></div>
    <div class="at on-dark reg" style="left:257px; top:1642px;">REG <sup>$</sup>237<sup>00</sup></div>
    <div class="divider" style="left:487px; top:1566px; height:93px;"></div>
    <div class="at price-pill" style="left:713px; top:1584px;"><sup>$</sup>225<sup>00</sup></div>
    <div class="at on-dark note" style="left:713px; top:1643px;">(Limited Deal)</div>

    <div class="at includes-pill" style="left:486px; top:1698px;">INCLUDES</div>
    <div class="at on-dark package-list" style="left:486px; top:1766px;">
      <span class="bullet-dot">•</span> Video Analysis &nbsp;<span class="bullet-dot">•</span> Lesson Summary And Video Review Sent<br>
      To Mobile Devices &nbsp;<span class="bullet-dot">•</span> Tips And Drills &nbsp;<span class="bullet-dot">•</span> Action Plan To Improve
    </div>

    <!-- Credentials -->
    <div class="at credential" style="left:486px; top:1903px;">WES HADLEY<br>CLASS A MEMBER<br>QTR</div>
    <div class="at credential" style="left:486px; top:2003px;">CENTURY<br>MEMBER NLT</div>
    <div class="at credential" style="left:792px; top:2032px; font-size:22px;">WES HADLEY</div>

    <!-- Contact -->
    <div class="at footer-text" style="left:182px; top:2142px;">whadley@NLT.com</div>
    <div class="at footer-sep" style="left:347px; top:2142px;">|</div>
    <div class="at footer-text strong" style="left:488px; top:2142px;">410-555-0182</div>
    <div class="at footer-sep" style="left:637px; top:2142px;">|</div>
    <div class="at footer-text" style="left:792px; top:2142px;">WHADLEY.COM</div>
  </main>
</body>
</html>
```